Cleaning Company needs a new business card design

Hi, We are looking for new business card designs to update with our latest logo and company information.
We would like to see designs using the colours:
Royal Blue #4169E1 - this is our company colour so this has to be in there. Please feel free to experiment with other colours.
Must include:
Front of business card:
Logo
Back of the business card:
0800 529 6081
07438 915 702
Email: info@pkrtidyhomes.co.uk
Web: www.pkrtidyhomes.co.uk
Services:
End of Tenancy
Carpet & Upholstery
Regular & One Off
all work fully insured.
The front of the business card with the logo can be made to look raised print. The blue man to be a shiny finish.
The business card needs to be presented in a matt finish
The business must be in the following styles:
Standard Square with rounded corners.
Thank you to all that take part in this.
Target Market(s)
Men and Women of different ages in the UK.
Industry/Entity Type
House Cleaning
Contact Information for Business Card
Front of business card:
Logo
0800 529 6081
07438 915 702
Email: pkrtidy@mailbox-demo.co.uk
Services:
End of Tenancy
Carpet & Upholstery
Regular & One Off
all work fully insured.

```html
<!DOCTYPE html>
<html lang="en">
<head>
<meta charset="utf-8">
<title>PKR Tidy Homes – Business Card</title>
<link href="https://fonts.googleapis.com/css2?family=Questrial&family=Arimo:wght@400&display=swap" rel="stylesheet">
<style>
  :root {
    --brand-navy: #3b4290;
    --brand-sky: #35a8e0;
    --card-cream: #f3f2eb;
    --ink: #1e1e1e;
    --white: #ffffff;
  }
  * { margin: 0; padding: 0; box-sizing: border-box; }
  html, body {
    width: 1000px;
    height: 1200px;
    overflow: hidden;
    background: var(--white);
  }
  .canvas {
    position: relative;
    width: 1000px;
    height: 1200px;
  }
  .card {
    position: absolute;
    left: 101px;
    width: 797px;
  }
  .card--front {
    top: 25px;
    height: 562px;
    background: var(--brand-navy);
  }
  .card--back {
    top: 613px;
    height: 560px;
    background: var(--card-cream);
  }
  .brand {
    position: absolute;
    display: flex;
    align-items: center;
    gap: 22px;
    font-family: "Questrial", sans-serif;
    font-weight: 400;
    white-space: nowrap;
  }
  .brand__dot {
    flex: none;
    border-radius: 50%;
    background: var(--brand-sky);
  }
  .card--front .brand {
    left: 0;
    right: 0;
    top: 250px;
    justify-content: center;
    color: var(--white);
    font-size: 78px;
  }
  .card--front .brand__dot { width: 48px; height: 48px; }
  .card--back .brand {
    left: 38px;
    top: 100px;
    color: var(--brand-navy);
    font-size: 48px;
    gap: 14px;
  }
  .card--back .brand__dot { width: 30px; height: 30px; }
  .services {
    position: absolute;
    left: 38px;
    top: 392px;
    font-family: "Arimo", sans-serif;
    font-size: 26px;
    line-height: 32px;
    color: var(--ink);
    list-style: none;
  }
  .contact-band {
    position: absolute;
    left: 676px;
    top: 0;
    width: 121px;
    height: 560px;
    background: var(--brand-navy);
  }
  .contact-list {
    position: absolute;
    left: 14px;
    top: 537px;
    width: 300px;
    transform-origin: top left;
    transform: rotate(-90deg);
    list-style: none;
    font-family: "Arimo", sans-serif;
    font-size: 18.5px;
    line-height: 22.5px;
    color: var(--white);
    white-space: nowrap;
  }
</style>
</head>
<body>
<main class="canvas">
  <section class="card card--front" aria-label="Card front">
    <div class="brand">
      <span class="brand__dot" aria-hidden="true"></span>
      <span class="brand__name">PKR Tidy Homes</span>
    </div>
  </section>

  <section class="card card--back" aria-label="Card back">
    <div class="brand">
      <span class="brand__dot" aria-hidden="true"></span>
      <span class="brand__name">PKR Tidy Homes</span>
    </div>

    <ul class="services">
      <li>Services:</li>
      <li>End of Tenancy</li>
      <li>Carpet &amp; Upholstery</li>
      <li>Regular &amp; One Off</li>
    </ul>

    <aside class="contact-band">
      <ul class="contact-list">
        <li>0800 529 6081</li>
        <li>07438 915 702</li>
        <li>info@pkrtidyhomes.co.uk</li>
        <li>www.pkrtidyhomes.co.uk</li>
      </ul>
    </aside>
  </section>
</main>
</body>
</html>
```